Harbor Key Realty - New Agent Opportunity Overview

We want to create a one (1) page brochure to highlight what Harbor Key Realty (a real estate brokerage) offers new agents. I have uploaded a Word doc that has all the text we want on the flyer. We want a professional looking design.
Industry/Entity Type
Real Estate Agent
Colors
3176b5
33a6d7

```html
<!DOCTYPE html>
<html lang="en">
<head>
<meta charset="utf-8">
<title>Harbor Key Realty – New Agent Opportunity Overview</title>
<link href="https://fonts.googleapis.com/css2?family=Montserrat:wght@400;500;600;700&display=swap" rel="stylesheet">
<style>
  :root {
    --backdrop: #bdb9b7;
    --paper: #ffffff;
    --brand-blue: #4b55f2;
    --ink: #1d1d1f;
    --row-dark: #dedede;
    --row-light: #ececec;
    --white: #ffffff;
  }
  * { box-sizing: border-box; margin: 0; padding: 0; }
  html, body {
    width: 1200px; height: 780px; overflow: hidden;
    background: var(--backdrop);
    font-family: "Montserrat", sans-serif;
    color: var(--ink);
  }
  .flyer {
    position: absolute; left: 337px; top: 20px;
    width: 526px; height: 740px;
    background: linear-gradient(180deg, var(--paper) 0%, #f7f7f7 100%);
    padding: 30px 30px 0;
    box-shadow: 0 2px 10px rgba(0,0,0,0.12);
  }
  .brand-mark {
    height: 90px;
    display: flex; align-items: center; justify-content: center;
  }
  .brand-name {
    font-size: 33px; font-weight: 700; letter-spacing: 3px;
    text-transform: uppercase; color: var(--ink);
  }
  .opening-banner {
    margin-top: 28px; height: 90px;
    background: var(--brand-blue); color: var(--white);
    display: flex; flex-direction: column; justify-content: center; align-items: center;
    line-height: 1.12;
  }
  .opening-banner .location { font-size: 22.5px; font-weight: 500; }
  .opening-banner .announcement { font-size: 30.5px; font-weight: 700; }
  .tagline {
    margin-top: 24px; font-size: 11.3px; font-weight: 700;
    text-transform: uppercase; white-space: nowrap; letter-spacing: 0.1px;
  }
  .section-title {
    font-size: 14px; font-weight: 600; color: var(--brand-blue);
    margin-top: 18px; margin-bottom: 8px;
  }
  .feature-columns { display: flex; }
  .feature-list { list-style: none; padding-left: 15px; }
  .feature-columns .feature-list:first-child { width: 260px; }
  .feature-list li {
    font-size: 10.6px; line-height: 16.4px; position: relative; padding-left: 9px;
    white-space: nowrap;
  }
  .feature-list li::before {
    content: ""; position: absolute; left: 0; top: 6.6px;
    width: 4px; height: 4px; border-radius: 50%; background: var(--brand-blue);
  }
  .feature-list li.continued::before { display: none; }
  .split-table {
    margin-top: 20px; width: 100%;
    border-collapse: separate; border-spacing: 2px 2px; margin-left: -2px; width: calc(100% + 4px);
  }
  .split-table th {
    background: var(--brand-blue); color: var(--white);
    font-size: 13.5px; font-weight: 600; text-align: left;
    height: 20px; padding-left: 30px;
  }
  .split-table td { font-size: 10.6px; height: 20px; padding-left: 30px; }
  .split-table tr:nth-child(odd) td { background: var(--row-dark); }
  .split-table tr:nth-child(even) td { background: var(--row-light); }
  .split-table .col-split { padding-left: 54px; }
  .support-title { margin-top: 26px; }
</style>
</head>
<body>
  <article class="flyer">
    <header class="brand-mark">
      <span class="brand-name">Harbor Key Realty</span>
    </header>

    <section class="opening-banner">
      <span class="location">HKR Home Center Gaithersburg,</span>
      <span class="announcement">Maryland is Now Open!</span>
    </section>

    <p class="tagline">Ignite your real estate business – Join Harbor Key Realty</p>

    <h2 class="section-title">Consumer Direct Advantage</h2>
    <div class="feature-columns">
      <ul class="feature-list">
        <li>Lender Referrals</li>
        <li>Homestead Finder Leads</li>
        <li>Shared Lender Leads</li>
        <li>ListNest.com / NearbyHomesHub.com</li>
      </ul>
      <ul class="feature-list">
        <li>Credit Trigger Campaigns</li>
        <li>Consumer Behavior Campaigns</li>
        <li>HKR Call Center Marketing Team</li>
        <li>HKR Sponsored Local Events</li>
      </ul>
    </div>

    <h2 class="section-title">Maximized Compensation</h2>
    <ul class="feature-list">
      <li>No desk fees. No royalty fees. No franchise fees.</li>
      <li>Company paid E&amp;O</li>
      <li>Transaction fee of $550 includes Transaction Coordinator</li>
    </ul>

    <table class="split-table">
      <thead>
        <tr><th>Type of Deal</th><th class="col-split">Commission Split</th></tr>
      </thead>
      <tbody>
        <tr><td>Self-Generated</td><td class="col-split">90% / 10%</td></tr>
        <tr><td>Lender Referred Leads</td><td class="col-split">70% / 30%</td></tr>
        <tr><td>HKR Generated Leads / Referrals</td><td class="col-split">55% / 45%</td></tr>
      </tbody>
    </table>

    <h2 class="section-title support-title">Complete Support System</h2>
    <div class="feature-columns">
      <ul class="feature-list">
        <li>Powerful Suite of Cloud Based Tools</li>
        <li>IDX, CRM and Transaction Management</li>
        <li>HKR Call Center Support for Leads and Deals</li>
        <li>Transaction Coordinator</li>
        <li>Virtual Assistants Available</li>
      </ul>
      <ul class="feature-list">
        <li>24/7 Workspace Access</li>
        <li>Coaching / Mentoring</li>
        <li>Social Media / Marketing Expertise</li>
        <li>Nationwide Partnerships</li>
        <li class="continued">with Top Lenders</li>
      </ul>
    </div>
  </article>
</body>
</html>
```